Business Card Design

We require a Business card for a new business called Tallwood Coach Charter.
We offer Coach Charter/Transfers for sporting clubs, School groups, Elderly groups, business and for weddings around the ACT/NSW areas. Charters can be for a few hours,daily or out of town for several days or for groups coming into town and staying in the area.
We are a very small operation and would like our business card to have some colour and maybe something with a horizon and road travelled included. we are a company who likes to be helpful are friendly and have great customer service skills. we would like our card to represent our small but honest company. My partner has been in the Coach Industry for over 30 years and I myself for 10 years. Our coach is 57 seats and the colour is blue and silver.
Updates

To all designers

Thank you very much for your ideas and work put into a design for our business card
We hope to make a decision in the next few days, it is a tough decision as we really like a most of the designs put forward.
We hope to keep everyone updated a will let you know as soon as possible.

Thank you all again

We would just like to thank everyone for their Designs for our new Business card.

And to let you know we have finally made our choice.
Once again thank you and to let you know that this was a very hard decision and 
we would have liked to pick more than one.
Thanks to everyone again.

Target Market(s)

We have a very wide and varied customer field, would like to send business cards to the 120 Schools we have in our area at least.

Industry/Entity Type

Town

Contact Information for Business Card

Tallwood Coach Charter
Peter Maskell
24 Dunmore Place
Queanbeyan NSW 2620
ph: 0438192604
e-mail: peter.mk@mailvale.com

```html
<!DOCTYPE html>
<html lang="en">
<head>
<meta charset="utf-8">
<title>Tallwood Coach Charter – Business Card</title>
<link rel="stylesheet" href="https://fonts.googleapis.com/css2?family=EB+Garamond:wght@500&family=Open+Sans:wght@400&display=swap">
<style>
  :root {
    --navy: #02012e;
    --paper: #ffffff;
    --card-front: #fbfbfb;
    --lime: #ccff00;
    --rule-lime: #d6f05a;
    --rule-silver: #b9b9c6;
    --name-grey: #8c8c8c;
    --icon-grey: #6d6d66;
    --white: #ffffff;
  }
  * { margin: 0; padding: 0; box-sizing: border-box; }
  html, body { width: 896px; height: 1200px; overflow: hidden; background: var(--paper); }
  body { position: relative; }

  .card { position: absolute; overflow: hidden; }

  .card-front {
    left: 16px; top: 116px; width: 862px; height: 450px;
    background: var(--card-front);
  }
  .card-back {
    left: 99px; top: 685px; width: 698px; height: 429px;
    background: var(--navy);
  }

  .wordmark {
    position: absolute; left: 0; right: 0; text-align: center;
    font-family: "EB Garamond", serif; font-weight: 500; white-space: nowrap;
  }
  .card-front .wordmark-name {
    top: 133px; font-size: 104px; line-height: 1; color: var(--navy); letter-spacing: 1px;
  }
  .card-front .wordmark-rule {
    position: absolute; left: 91px; width: 669px; top: 241px; height: 1px; background: var(--rule-lime);
  }
  .card-front .wordmark-tag {
    top: 253px; font-size: 53px; line-height: 1; color: var(--navy); letter-spacing: 9px;
  }

  .card-back .wordmark-name {
    top: 55px; font-size: 68px; line-height: 1; color: var(--white);
  }
  .card-back .wordmark-rule {
    position: absolute; left: 0; right: 0; top: 120px; height: 1px; background: var(--rule-silver);
  }
  .card-back .wordmark-tag {
    top: 126px; font-size: 32px; line-height: 1; color: var(--white); letter-spacing: 5px;
  }

  .contact { font-family: "Open Sans", sans-serif; position: absolute; left: 0; right: 0; text-align: center; white-space: nowrap; }
  .contact-name { top: 197px; font-size: 28px; color: var(--name-grey); }
  .contact-address { top: 266px; font-size: 19px; color: var(--white); }
  .contact-lines {
    top: 298px; display: flex; justify-content: center; gap: 30px;
    font-size: 19px; color: var(--white);
  }
  .contact-item { display: flex; align-items: center; gap: 10px; }
  .contact-item svg { display: block; }

  .road-band {
    position: absolute; left: 0; right: 0; bottom: 0; height: 91px; background: var(--lime);
  }
  .road-dash {
    position: absolute; top: 40px; width: 58px; height: 10px; background: var(--white);
  }
</style>
</head>
<body>

<section class="card card-front" aria-label="Business card front">
  <div class="wordmark wordmark-name">TALLWOOD</div>
  <div class="wordmark-rule"></div>
  <div class="wordmark wordmark-tag">COACH CHARTER</div>
</section>

<section class="card card-back" aria-label="Business card back">
  <div class="wordmark wordmark-name">TALLWOOD</div>
  <div class="wordmark-rule"></div>
  <div class="wordmark wordmark-tag">COACH CHARTER</div>

  <p class="contact contact-name">Peter Maskell</p>
  <p class="contact contact-address">24 Dunmore Place Queanbeyan NSW 2620</p>
  <div class="contact contact-lines">
    <span class="contact-item">
      <svg width="30" height="30" viewBox="0 0 30 30" aria-hidden="true">
        <rect width="30" height="30" rx="4" fill="var(--icon-grey)"/>
        <path d="M11 6 C8 8 8 13 10 18 C12 23 16 26 19 25 L21 22 L18 19 L16 21 C14 19 13 16 13 13 L15 12 L13 7 Z" fill="none" stroke="#fff" stroke-width="1.6" stroke-linejoin="round"/>
      </svg>
      ph: 0438192604
    </span>
    <span class="contact-item">
      <svg width="34" height="24" viewBox="0 0 34 24" aria-hidden="true">
        <rect width="34" height="24" fill="var(--icon-grey)"/>
        <rect x="3" y="3" width="28" height="18" fill="#fff"/>
        <path d="M3 3 L17 14 L31 3 M3 21 L14 11 M31 21 L20 11" fill="none" stroke="var(--icon-grey)" stroke-width="2"/>
      </svg>
      e-mail: peter.mk@mailvale.com
    </span>
  </div>

  <div class="road-band">
    <span class="road-dash" style="left:30px"></span>
    <span class="road-dash" style="left:146px"></span>
    <span class="road-dash" style="left:261px"></span>
    <span class="road-dash" style="left:377px"></span>
    <span class="road-dash" style="left:492px"></span>
    <span class="road-dash" style="left:607px"></span>
  </div>
</section>

</body>
</html>
```